Business cards, letterhead, envelopes for Business Brokerage Firm
Business cards, letterhead, envelopes, fax cover sheet, postcards
Business cards, letterhead, envelopes for Business Brokerage Firm -
Creative Brief
Professional
Marek Dunholt
President
438 North Ferris Lane, Suite #516 Streamwood, Illinois 60107
marek@kelvrabusinessbrokers.com
www.kelvrabusinessbrokers.com
we do not have a slogan yet, if you have any ideas, feel free to add it in. We like the blues and grays for color.
We Sell Businesses -company sales or mergers -restaurant sales specialist -commercial real estate sales -exit/sale strategy consulting -operations consulting -estimates of value

```html
<!DOCTYPE html>
<html lang="en">
<head>
<meta charset="utf-8">
<title>Kelvra Business Brokers — Stationery</title>
<link rel="stylesheet" href="https://fonts.googleapis.com/css2?family=EB+Garamond:wght@400;500&display=swap">
<style>
  :root {
    --backdrop: #e7e8ea;
    --paper: #ffffff;
    --brand-blue: #3d6585;
    --flap-blue: #3a5f7d;
    --ink-gray: #5b6873;
    --rule: #8ea3b4;
    --photo-tone: linear-gradient(160deg, #8b8f94, #3f4650);
  }
  * { box-sizing: border-box; margin: 0; padding: 0; }
  html, body { width: 1200px; height: 707px; overflow: hidden; }
  body {
    background: var(--backdrop);
    font-family: "EB Garamond", "Times New Roman", serif;
    color: var(--ink-gray);
    position: relative;
  }
  .sheet { position: absolute; background: var(--paper); overflow: hidden; }

  /* Brand name lockup */
  .brand { display: flex; align-items: flex-start; gap: 6px; color: var(--brand-blue); }
  .brand-dot { border-radius: 50%; background: var(--brand-blue); flex: none; }
  .brand-name { text-transform: uppercase; font-weight: 500; line-height: 1.05; letter-spacing: .04em; white-space: nowrap; }

  .footer-rule { position: absolute; height: 1px; background: var(--rule); }
  .footer-text { position: absolute; font-size: 5.2px; text-align: center; line-height: 1.4; color: var(--ink-gray); white-space: nowrap; }

  /* Business card front */
  .card-front { left: 34px; top: 283px; width: 124px; height: 89px; }
  .card-photo { position: absolute; left: 5px; top: 6px; width: 32px; height: 42px; background: var(--photo-tone); }
  .card-person { position: absolute; right: 7px; top: 8px; text-align: right; }
  .card-person .name { font-size: 7px; color: var(--ink-gray); font-weight: 500; }
  .card-person .title { font-size: 5px; }
  .card-front .brand { position: absolute; left: 44px; top: 32px; }
  .card-front .brand-dot { width: 7px; height: 7px; margin-top: 2px; }
  .card-front .brand-name { font-size: 5.6px; }
  .card-front .footer-rule { left: 4px; right: 4px; top: 60px; }
  .card-front .footer-text { left: 4px; top: 63px; font-size: 3.6px; text-align: left; }

  /* Business card back */
  .card-back { left: 34px; top: 384px; width: 124px; height: 96px; }
  .card-back .brand { position: absolute; left: 8px; top: 10px; }
  .card-back .brand-dot { width: 9px; height: 9px; margin-top: 2px; }
  .card-back .brand-name { font-size: 6.4px; }
  .services { position: absolute; top: 52px; font-size: 4.3px; line-height: 1.35; white-space: nowrap; }
  .services.left { left: 8px; }
  .services.right { left: 66px; }

  /* Letterhead */
  .letterhead { left: 233px; top: 79px; width: 434px; height: 607px; }
  .letterhead .brand { position: absolute; left: 22px; top: 14px; }
  .letterhead .brand-dot { width: 20px; height: 20px; }
  .letterhead .brand-name { font-size: 9px; }
  .letterhead .footer-rule { left: 22px; right: 22px; top: 548px; }
  .letterhead .footer-text { left: 22px; right: 22px; top: 553px; }

  /* Envelope back */
  .envelope-back { left: 696px; top: 79px; width: 456px; height: 221px; }
  .envelope-back svg { position: absolute; left: 0; top: 0; }

  /* Envelope front */
  .envelope-front { left: 696px; top: 367px; width: 456px; height: 317px; }
  .envelope-front .brand { position: absolute; left: 17px; top: 40px; }
  .envelope-front .brand-dot { width: 22px; height: 22px; }
  .envelope-front .brand-name { font-size: 9.5px; }
  .envelope-front .footer-rule { left: 17px; right: 17px; top: 264px; }
  .envelope-front .footer-text { left: 17px; right: 17px; top: 268px; }
</style>
</head>
<body>

  <section class="sheet card-front" aria-label="Business card front">
    <div class="card-photo" role="img" aria-label="Portrait photo of Marek Dunholt"></div>
    <div class="card-person">
      <p class="name">Marek Dunholt</p>
      <p class="title">President</p>
    </div>
    <div class="brand">
      <span class="brand-dot"></span>
      <p class="brand-name">Kelvra<br>Business<br>Brokers</p>
    </div>
    <div class="footer-rule"></div>
    <p class="footer-text">Address: 438 North Ferris Lane, Suite #516 Streamwood, Illinois 60107<br>Tel: (847) 555-0142 &nbsp; Fax: (847) 555-0143<br>marek@kelvrabusinessbrokers.com &nbsp; www.kelvrabusinessbrokers.com</p>
  </section>

  <section class="sheet card-back" aria-label="Business card back">
    <div class="brand">
      <span class="brand-dot"></span>
      <p class="brand-name">Kelvra<br>Business<br>Brokers</p>
    </div>
    <p class="services left">company sales or mergers<br>restaurant sales specialist<br>commercial real estate sales</p>
    <p class="services right">exit/sale strategy consulting<br>operations consulting<br>estimates of value</p>
  </section>

  <section class="sheet letterhead" aria-label="Letterhead">
    <div class="brand">
      <span class="brand-dot"></span>
      <p class="brand-name">Kelvra<br>Business<br>Brokers</p>
    </div>
    <div class="footer-rule"></div>
    <p class="footer-text">Address: 438 North Ferris Lane, Suite #516 Streamwood, Illinois 60107 &nbsp; Tel: (847) 555-0142 &nbsp; Fax: (847) 555-0143<br>Email: marek@kelvrabusinessbrokers.com &nbsp; Web: www.kelvrabusinessbrokers.com</p>
  </section>

  <section class="sheet envelope-back" aria-label="Envelope back">
    <svg width="456" height="221" viewBox="0 0 456 221" aria-hidden="true">
      <polygon points="0,0 456,0 456,22 250,100 206,100 0,22" fill="var(--flap-blue)"/>
    </svg>
  </section>

  <section class="sheet envelope-front" aria-label="Envelope front">
    <div class="brand">
      <span class="brand-dot"></span>
      <p class="brand-name">Kelvra<br>Business<br>Brokers</p>
    </div>
    <div class="footer-rule"></div>
    <p class="footer-text">Address: 438 North Ferris Lane, Suite #516 Streamwood, Illinois 60107 &nbsp; Tel: (847) 555-0142<br>Email: marek@kelvrabusinessbrokers.com &nbsp; Web: www.kelvrabusinessbrokers.com</p>
  </section>

</body>
</html>
```